Data Analytics Irish company needs Stationery Design

We need a stationery design for our data analytics company based in Dublin called 'Numbryx': we develop innovative web-based corporate applications exploiting advanced Machine Learning and Data Mining techniques.
Like the animal that inspired our company name, the final design should communicate intelligence and passion; on the other hand, we want to keep the highest professional appeal.
We love our current logo and we have tried out several color variations: we prefer solutions (see the logo attached) with white design and dark backgrounds, but we will also be glad to see some designs that follow the colors of the palette of the attached web screenshot.

```html
<!DOCTYPE html>
<html lang="en">
<head>
<meta charset="utf-8">
<title>Numbryx Envelope Stationery</title>
<link href="https://fonts.googleapis.com/css2?family=Arimo:wght@400;600&display=swap" rel="stylesheet">
<style>
  :root {
    --backdrop: #d1d2d4;
    --envelope-front: #354657;
    --envelope-back: #2a313b;
    --envelope-flap: #34475a;
    --ink-muted: #9aa1a8;
    --ink-light: #c9ced3;
    --mark-faint: #3b4450;
  }
  * { margin: 0; padding: 0; box-sizing: border-box; }
  html, body {
    width: 1200px; height: 1000px; overflow: hidden;
    background: var(--backdrop);
    font-family: "Arimo", Arial, sans-serif;
  }
  .stage { position: relative; width: 1200px; height: 1000px; }
  .envelope {
    position: absolute; left: 279px; width: 624px; height: 312px;
    box-shadow: 0 6px 10px rgba(0,0,0,0.22);
  }
  .envelope--front { top: 130px; background: var(--envelope-front); }
  .envelope--back { top: 534px; background: var(--envelope-back); overflow: hidden; }

  .brand-name {
    position: absolute; left: 64px; top: 77px;
    font-size: 22px; font-weight: 600; letter-spacing: 0.3px;
    color: var(--ink-muted);
  }
  .sender-line {
    position: absolute; left: 64px; top: 117px;
    font-size: 10px; color: var(--ink-muted);
  }
  .contact-block {
    position: absolute; left: 403px; top: 179px;
    font-size: 10.5px; line-height: 14px; letter-spacing: 0.7px;
    color: var(--ink-muted); font-style: normal;
  }
  .web-address {
    position: absolute; left: 403px; top: 266px;
    font-size: 10.5px; letter-spacing: 0.7px; color: var(--ink-light);
  }
  .flap { position: absolute; left: 0; top: 0; }
  .faint-mark {
    position: absolute; left: 222px; top: 116px;
    width: 168px; height: 168px; border-radius: 50%;
    background: var(--mark-faint);
  }
</style>
</head>
<body>
  <main class="stage">
    <section class="envelope envelope--front" aria-label="Envelope front">
      <div class="brand-name">Numbryx</div>
      <div class="sender-line">Quay Road 555</div>
      <address class="contact-block">
        Quay Road 555<br>
        tel: 123-555-0147<br>
        fax: 123-555-0148<br>
        anna@numbryx.com
      </address>
      <div class="web-address">www.numbryx.com</div>
    </section>

    <section class="envelope envelope--back" aria-label="Envelope back">
      <svg class="flap" width="624" height="100" viewBox="0 0 624 100" aria-hidden="true">
        <polygon points="0,0 624,0 596,98 28,98" fill="var(--envelope-flap)"/>
      </svg>
      <div class="faint-mark" aria-hidden="true"></div>
    </section>
  </main>
</body>
</html>
```